Business Card Design

Business card for investment firm. I would like a two-sided card with the logo on a white front and then a solid back (the accent color or gray) with the leaf in a slightly lighter shade of that color. I would like the logo portion of the card to be debossed. I have attached some pictures of front of cards that I like. Note that on the Harborline Bank & Trust card; that is an example where we could use the white logo on green/blue on the strip at the top and then the back would be white with the actual regular logo.

For the feel of the card, here are some Industry examples of my competitors:
wwww.tvelqro.com
www.brightwoodcapital.com
www.wrenfold-advisors.com
www.plumhollowcap.com
www.tideharborpartners.com
www.venmoor.com
www.quillharth.com
www.zup.com
www.faywickellc.com
www.pellomarfunds.com

Target Market(s)

Institutional investors and high net worth individuals

Industry/Entity Type

Investment

Requirements
Must have
• Must be a clean design. I don't want the card to look cluttered.

```html
<!DOCTYPE html>
<html lang="en">
<head>
<meta charset="utf-8">
<title>Ashgrove Equity Partners — Business Card</title>
<link href="https://fonts.googleapis.com/css2?family=Cinzel:wght@400;600;700&display=swap" rel="stylesheet">
<style>
  :root {
    --canvas: #e9e7e3;
    --card: #ffffff;
    --navy: #1d2a4d;
    --ink: #5a5a5a;
    --leaf-blue: #b7c1d1;
    --leaf-blue-soft: #c9d1de;
    --shadow: rgba(40, 30, 20, 0.18);
  }
  * { box-sizing: border-box; margin: 0; padding: 0; }
  html, body {
    width: 1200px;
    height: 857px;
    overflow: hidden;
    background: var(--canvas);
    font-family: "Cinzel", "Times New Roman", serif;
  }
  .canvas {
    width: 1200px;
    height: 857px;
    display: flex;
    align-items: center;
    justify-content: center;
    gap: 40px;
  }
  .card {
    position: relative;
    width: 560px;
    height: 320px;
    background: var(--card);
    box-shadow: 0 10px 28px var(--shadow);
    overflow: hidden;
  }

  /* Front */
  .brand {
    position: absolute;
    left: 44px;
    top: 108px;
    display: flex;
    align-items: center;
    gap: 12px;
    color: var(--navy);
  }
  .brand__dot {
    width: 14px;
    height: 14px;
    border-radius: 50%;
    background: var(--navy);
  }
  .brand__name {
    font-weight: 600;
    font-size: 24px;
    letter-spacing: 0.04em;
    line-height: 1.1;
  }
  .brand__name small {
    display: block;
    font-size: 10px;
    letter-spacing: 0.22em;
  }
  .contact {
    position: absolute;
    left: 300px;
    top: 86px;
    color: var(--ink);
    font-size: 11px;
    letter-spacing: 0.06em;
    line-height: 1.35;
  }
  .contact__name {
    font-weight: 700;
    font-size: 17px;
    letter-spacing: 0.06em;
  }
  .contact__title {
    font-size: 8.5px;
    font-weight: 600;
    letter-spacing: 0.08em;
    margin-bottom: 18px;
  }
  .contact__address { margin-bottom: 6px; }
  .contact__phones span {
    display: inline-block;
    width: 12px;
    color: var(--navy);
    font-weight: 700;
  }
  .contact__email { margin-top: 14px; }

  /* Back */
  .mark-area {
    position: absolute;
    inset: 0;
    width: 560px;
    height: 320px;
  }
  .web {
    position: absolute;
    left: 26px;
    bottom: 24px;
    color: var(--ink);
    font-size: 11px;
    letter-spacing: 0.1em;
  }
</style>
</head>
<body>
  <main class="canvas">
    <section class="card card--front" aria-label="Card front">
      <div class="brand">
        <span class="brand__dot"></span>
        <div class="brand__name">ASHGROVE<small>EQUITY PARTNERS</small></div>
      </div>
      <div class="contact">
        <div class="contact__name">DANIEL REEVES</div>
        <div class="contact__title">PRESIDENT &amp; CEO</div>
        <div class="contact__address">418 MERIDIAN AVENUE<br>SUITE 210<br>AUSTIN, TX 78704</div>
        <div class="contact__phones">
          <div><span>T</span>512.555.0142</div>
          <div><span>F</span>512.555.0187</div>
          <div><span>C</span>512.555.0163</div>
        </div>
        <div class="contact__email">DANIEL@ASHGROVECAP.COM</div>
      </div>
    </section>

    <section class="card card--back" aria-label="Card back">
      <svg class="mark-area" viewBox="0 0 560 320" role="img" aria-label="Large pale blue brand mark decoration across the upper and right area">
        <defs>
          <linearGradient id="markTone" x1="0" y1="0" x2="1" y2="1">
            <stop offset="0" stop-color="#b7c1d1"/>
            <stop offset="1" stop-color="#c9d1de"/>
          </linearGradient>
        </defs>
        <path d="M70 0 H560 V320 H300 C296 262 250 228 180 222 C120 218 60 214 0 208 V46 C24 34 50 16 70 0 Z" fill="url(#markTone)"/>
      </svg>
      <div class="web">WWW.ASHGROVECAP.COM</div>
    </section>
  </main>
</body>
</html>
```